Web site for cutting edge executive coaching and consulting firm | ||
Bravonte | ||
Consulting | ||
Services that increase Performance: - Coaching: Executives, Groups / Teams - Problem Solving - Organizational Change. Focus on: - Holistic approach - Verdessan spirit (colors) - Psychological driven models - Relationship building - sustained outcomes |
I like colors, yet, colors shall not hinder clear reading of text. I like a clear & simple structure of Website. I like to use symbols and/or forms. |
Cutting-Edge Unique/Creative Clean/Simple Professional Exciting Industrial Colorful Elegant Progressive Service Oriented Traditional |
blue | ||
Arial Verdana |

```html
<!DOCTYPE html>
<html lang="en">
<head>
<meta charset="UTF-8">
<title>Bravonte Consulting</title>
<link rel="stylesheet" href="https://fonts.googleapis.com/css2?family=Arimo:wght@400;700&family=Tinos:ital,wght@1,700&display=swap">
<style>
:root{
  --blue-deep:#1d3f9c;
  --blue:#2a5bc4;
  --blue-light:#4f8ee0;
  --navy:#1f3b8f;
  --red:#c21a1a;
  --red-dark:#8c0e0e;
  --text:#3a3a3a;
  --muted:#777;
  --line:#d9d9d9;
  --footer:#6d7785;
  --footer-text:#eef1f5;
  --page:#ffffff;
}
*{margin:0;padding:0;box-sizing:border-box}
html,body{width:1200px;height:888px;overflow:hidden;background:var(--page);font-family:Arimo,Arial,sans-serif;color:var(--text)}
.page{position:relative;width:1200px;height:888px}

.brand{position:absolute;left:168px;top:50px;font-size:54px;font-weight:700;color:var(--navy);letter-spacing:-1px;line-height:1}
.brand-tag{position:absolute;left:268px;top:46px;font-size:11px;font-weight:700;letter-spacing:3px;color:var(--navy);white-space:nowrap}

.phone{position:absolute;left:895px;top:38px;display:flex;align-items:center;gap:10px;font-size:19px;font-weight:700;color:var(--navy)}
.phone svg{width:22px;height:22px}

.nav{position:absolute;top:90px;left:560px;font-size:15px;font-weight:700;color:#555}
.nav a{position:absolute;white-space:nowrap;color:#555;text-decoration:none}
.nav .active{color:var(--red)}
.nav .pin{position:absolute;left:0;top:-2px;width:12px;height:20px}

.hero{position:absolute;left:161px;top:127px;width:878px;height:319px;background:linear-gradient(180deg,var(--blue-light) 0%,var(--blue) 45%,var(--blue-deep) 100%);box-shadow:0 3px 8px rgba(0,0,0,.3)}
.hero-quote{position:absolute;left:45px;top:90px;width:330px;font-size:20px;line-height:1.3;color:#fff}
.btn-hero{position:absolute;left:45px;top:221px;width:135px;height:36px;border-radius:5px;background:linear-gradient(180deg,#e13030,var(--red-dark));color:#fff;font-size:16px;font-weight:700;display:flex;align-items:center;justify-content:center;box-shadow:0 2px 4px rgba(0,0,0,.4)}
.dots{position:absolute;left:55px;top:288px;display:flex;gap:8px}
.dots span{width:13px;height:13px;border-radius:50%;background:#fff;border:2px solid #9bbbe8}
.dots .on{background:var(--navy)}
.video{position:absolute;left:396px;top:29px;width:444px;height:283px;background:#000}
.video .bar{position:absolute;left:0;bottom:0;width:100%;height:24px;background:linear-gradient(#f4f4f4,#cfcfcf)}
.video .prog{position:absolute;left:0;bottom:24px;width:100%;height:4px;background:#999}

.col{position:absolute;top:470px;width:240px}
.col h2{font-size:17px;font-weight:700;color:var(--navy);margin-bottom:14px}
.col p{font-size:11.5px;line-height:1.45;color:var(--text)}
.col-welcome{left:168px}
.col-services{left:475px}
.col-news{left:770px}
.divider{position:absolute;top:466px;width:1px;height:280px;background:var(--line)}
.photo{width:224px;height:124px;background:linear-gradient(135deg,#e6e9ee,#b9c2cf 60%,#8a8f99);border:1px solid #ccc;margin-bottom:14px}
.more{display:inline-block;margin-top:8px;padding:3px 9px;border-radius:8px;background:linear-gradient(#d32222,var(--red-dark));color:#fff;font-size:10px;font-weight:700}
.services{list-style:none;margin:12px 0 0 12px}
.services li{font-size:11.5px;font-weight:700;color:var(--red);line-height:1.9;position:relative;padding-left:12px}
.services li::before{content:"";position:absolute;left:0;top:8px;width:5px;height:5px;background:var(--red);border-radius:50%}
.news-title{font-family:Tinos,'Times New Roman',serif;font-style:italic;font-weight:700;font-size:11px;color:#555}
.news-date{font-size:10px;font-weight:700;color:#333;margin:4px 0 10px}
.news-body{color:var(--muted)!important}

.footer{position:absolute;left:0;top:773px;width:1200px;height:115px;background:var(--footer)}
.footer-links{position:absolute;left:163px;top:20px;font-size:12px;color:var(--footer-text)}
.footer-copy{position:absolute;left:163px;top:42px;font-size:11px;color:var(--footer-text)}
.social{position:absolute;left:920px;top:26px;display:flex;gap:12px}
.social span{width:33px;height:33px;border-radius:6px;background:linear-gradient(#8fb3e8,#3c6bc0);box-shadow:0 1px 3px rgba(0,0,0,.3)}
</style>
</head>
<body>
<div class="page">
  <header>
    <div class="brand">Bravonte</div>
    <div class="brand-tag">CLEAR PATHWAYS</div>
    <div class="phone">
      <svg viewBox="0 0 22 22"><circle cx="11" cy="11" r="11" fill="var(--navy)"/><path d="M7.5 6c1 0 1.5 2 1.8 3 .2.7-1 1.2-.8 1.8.5 1.2 1.5 2.2 2.7 2.7.6.2 1.1-1 1.8-.8 1 .3 3 .8 3 1.8 0 1-1.3 2-2.5 2C9.5 16.5 5.5 12.5 5.5 8.5 5.5 7.3 6.5 6 7.5 6z" fill="#fff"/></svg>
      <span>1800-555-0142</span>
    </div>
    <nav class="nav">
      <svg class="pin" viewBox="0 0 12 20"><circle cx="6" cy="4" r="3" fill="var(--red)"/><rect x="5" y="8" width="2" height="11" fill="var(--red)"/></svg>
      <a class="active" style="left:18px">Home</a>
      <a style="left:88px">About</a>
      <a style="left:160px">Services</a>
      <a style="left:246px">News</a>
      <a style="left:311px">Contact us</a>
      <a style="left:412px">Members</a>
    </nav>
  </header>

  <section class="hero">
    <p class="hero-quote">The significant problems we have, cannot be solved at the same level of thinking with which we created them.</p>
    <div class="btn-hero">LEARN MORE</div>
    <div class="dots"><span class="on"></span><span></span><span></span><span></span><span></span></div>
    <div class="video" role="img" aria-label="Introductory video player">
      <div class="prog"></div>
      <div class="bar"></div>
    </div>
  </section>

  <div class="divider" style="left:451px"></div>
  <div class="divider" style="left:746px"></div>

  <section class="col col-welcome">
    <h2>Welcome to Bravonte</h2>
    <div class="photo" role="img" aria-label="Photo of executives in a coaching meeting"></div>
    <p>Lorem ipsum dolor sit amet, consectetuer adipiscing elit, sed diam nonummy nibh euismod tincidunt ut laoreet dolore magna aliquam erat volutpat. Ut wisi enim ad minim veniam.</p>
    <span class="more">read more</span>
  </section>

  <section class="col col-services">
    <h2>Our Services</h2>
    <p>Lorem ipsum dolor sit amet, consectetuer adipiscing elit, sed diam nonummy nibh euismod tincidunt ut laoreet dolore magna aliquam erat volutpat. Ut wisi enim ad minim veniam.</p>
    <ul class="services">
      <li>Coaching</li>
      <li>Relation Building</li>
      <li>Problem Solving</li>
    </ul>
    <span class="more">read more</span>
  </section>

  <section class="col col-news">
    <h2>Latest News</h2>
    <div class="news-title">Lorem ipsum dolor sit amet</div>
    <div class="news-date">November 7, 2010</div>
    <p class="news-body">Lorem ipsum dolor sit amet, consectetuer adipiscing elit, sed diam nonummy nibh euismod tincidunt ut laoreet dolore magna aliquam erat volutpat. Ut wisi enim ad minim veniam.</p>
    <span class="more">read more</span>
  </section>

  <footer class="footer">
    <div class="footer-links">Home &nbsp;|&nbsp; About Us &nbsp;|&nbsp; Our Services &nbsp;|&nbsp; | &nbsp;Testimonials &nbsp;|&nbsp; Contact Us</div>
    <div class="footer-copy">copyright Bravonte Clear Pathways. All rights reserved.</div>
    <div class="social"><span></span><span></span><span></span></div>
  </footer>
</div>
</body>
</html>
```